Frozen Yoghurt - Treue Pass
Wir fuehren gerade ein neues Produkt ein, den Frozen Yogurt.
Es ist eine Treue Karte. Wer 10 x kauft bekommt eines Gratis. Detailinformation von unserem Fokus Team wurden skizziert und werden eingescannt.
Bei den Produktskizzen haetten wir gerne mit Zeichnung die einfach gezeichnet wirken. Wie eine Karikatur evtl. nur Umrisse und schwarz weiss.
Jede Karikatur darf dann ein Element in einer Kraeftigen Farbe haben. z.B. wo steht Fruechte ware dann z. B eine schoene rote Erdbeere etc.
Die detailiierten Infos sind auf den eingescannten skizzen. Auch die Abmessungen fuer den Druck.
Bei weiteren Infos geben wir gerne einfach fragen...
Vielen Dank im Voraus und viel Spass

```html
<!DOCTYPE html>
<html lang="de">
<head>
<meta charset="utf-8">
<title>Frozen Yoghurt Pass</title>
<link rel="stylesheet" href="https://fonts.googleapis.com/css2?family=Fredoka:wght@500;600&family=Arimo:wght@400;700&display=swap">
<style>
  :root {
    --green: #86b82a;
    --green-light: #c9dc8f;
    --cream: #fdf0cf;
    --cream-pale: #f4f1dc;
    --purple: #3d2340;
    --white: #ffffff;
    --orange: #e99a2b;
    --choc: #5a3419;
    --berry: #c1245a;
    --coffee: #6a3f1e;
  }
  * { margin: 0; padding: 0; box-sizing: border-box; }
  html, body { width: 1200px; height: 628px; overflow: hidden; background: var(--white); }
  body { position: relative; font-family: "Arimo", Arial, sans-serif; color: var(--purple); }
  .abs { position: absolute; }

  /* front strip */
  .front { left: 0; top: 0; width: 1200px; height: 285px; }
  .front-main {
    left: 0; top: 0; width: 999px; height: 285px;
    background: radial-gradient(ellipse 70% 110% at 52% 100%, var(--cream-pale) 0%, #dce8b4 45%, var(--green) 100%);
  }
  .front-title {
    left: 184px; top: 2px; font-family: "Fredoka", sans-serif; font-weight: 600;
    font-size: 38px; letter-spacing: 0.5px; white-space: nowrap;
  }
  .cup { width: 116px; height: 172px; top: 55px; border-radius: 50% 50% 14px 14px / 40% 40% 14px 14px; }
  .cup-muesli { left: 77px; background: linear-gradient(var(--white) 15%, var(--orange) 40%, var(--white) 62%); }
  .cup-schoggi { left: 319px; background: linear-gradient(var(--white) 15%, var(--choc) 40%, var(--white) 62%); }
  .cup-fruecht { left: 557px; background: linear-gradient(var(--white) 15%, var(--berry) 40%, var(--white) 62%); }
  .cup-kafi { left: 794px; background: linear-gradient(var(--white) 15%, var(--coffee) 40%, var(--white) 62%); }
  .flavour {
    top: 246px; width: 160px; text-align: center; font-family: "Fredoka", sans-serif;
    font-weight: 600; font-size: 20px;
  }
  .fold-line { width: 0; border-left: 2px dashed var(--purple); }
  .coupon { left: 999px; top: 0; width: 201px; height: 285px; background: var(--cream); }
  .coupon-badge {
    left: 25px; top: 40px; width: 152px; height: 152px; border-radius: 50%;
    border: 2px dotted var(--purple);
    background: radial-gradient(circle, var(--white) 30%, var(--green-light) 70%);
  }
  .coupon-title { left: 0; top: 222px; width: 201px; text-align: center; font-family: "Fredoka", sans-serif; font-weight: 600; font-size: 20px; }
  .coupon-note { left: 0; top: 255px; width: 201px; text-align: center; font-size: 9px; }

  /* back strip */
  .back { left: 0; top: 342px; width: 1200px; height: 286px; background: var(--cream); }
  .back-panel { left: 0; top: 0; width: 200px; height: 286px; background: var(--green); }
  .write-line { top: 40px; width: 2px; height: 232px; background: #6d6d6d; }
  .write-label { font-size: 9px; transform: rotate(-90deg); transform-origin: left top; white-space: nowrap; }

  .facts { left: 263px; top: 16px; width: 337px; list-style: none; }
  .fact {
    background: var(--green); color: var(--purple); font-size: 14px; line-height: 19px;
    padding: 3px 10px 3px 16px; margin-bottom: 13px;
  }
  .fact::before { content: "•"; margin-right: 8px; }

  .social { left: 620px; top: 14px; width: 70px; height: 190px; }
  .social-text {
    position: absolute; left: 58px; top: 0; width: 190px; font-size: 9px; line-height: 12px;
    transform: rotate(90deg); transform-origin: left top;
  }
  .social-mark { left: 624px; top: 205px; width: 20px; height: 20px; background: #3b5a9a; }

  .brand-mark { left: 263px; top: 243px; width: 30px; height: 30px; background: var(--green); }
  .brand-name { left: 316px; top: 251px; font-size: 9px; color: var(--green); }
  .slogan { left: 316px; top: 264px; font-size: 15px; color: var(--green); }

  .pass-title { left: 780px; top: 10px; font-family: "Fredoka", sans-serif; font-weight: 600; font-size: 36px; white-space: nowrap; }
  .stamps {
    left: 755px; top: 74px; width: 428px; height: 171px; border-collapse: collapse;
  }
  .stamps td { border: 2px solid var(--purple); width: 20%; text-align: center; vertical-align: middle; }
  .stamps td.stamp-free { background: var(--green); }
  .stamp-cup { display: inline-block; width: 38px; height: 56px; border-radius: 50% 50% 6px 6px / 40% 40% 6px 6px; }
  .tone-berry { background: linear-gradient(var(--white) 10%, #cf6b7a 40%, var(--white) 62%); }
  .tone-choc { background: linear-gradient(var(--white) 10%, #8a5a34 40%, var(--white) 62%); }
  .tone-orange { background: linear-gradient(var(--white) 10%, #eeb064 40%, var(--white) 62%); }
  .tone-free { background: linear-gradient(var(--white) 10%, #5e6a56 40%, #dfe8c2 62%); }
  .pass-note { left: 755px; top: 260px; width: 428px; text-align: center; font-size: 14px; }
</style>
</head>
<body>

<section class="front abs" aria-label="Vorderseite">
  <div class="front-main abs">
    <h1 class="front-title abs">frozen yoghurt : diis ding für e summer</h1>
    <div class="cup cup-muesli abs" role="img" aria-label="Illustration: Frozen Yoghurt im Becher mit Müesli"></div>
    <div class="cup cup-schoggi abs" role="img" aria-label="Illustration: Frozen Yoghurt im Becher mit Schoggi"></div>
    <div class="cup cup-fruecht abs" role="img" aria-label="Illustration: Frozen Yoghurt im Becher mit Früchten"></div>
    <div class="cup cup-kafi abs" role="img" aria-label="Illustration: Frozen Yoghurt im Becher mit Kafi"></div>
    <p class="flavour abs" style="left:55px">müesli</p>
    <p class="flavour abs" style="left:297px">schoggi</p>
    <p class="flavour abs" style="left:535px">frücht</p>
    <p class="flavour abs" style="left:772px">kafi</p>
  </div>
  <div class="fold-line abs" style="left:998px; top:0; height:285px"></div>
  <div class="coupon abs">
    <div class="coupon-badge abs" role="img" aria-label="Illustration: Gratis-Becher Frozen Yoghurt im Strahlenkreis"></div>
    <p class="coupon-title abs">gratis</p>
    <p class="coupon-note abs">fresh corner @ markt ecke</p>
  </div>
</section>

<section class="back abs" aria-label="Rückseite">
  <div class="back-panel abs">
    <div class="write-line abs" style="left:58px"></div>
    <div class="write-line abs" style="left:113px"></div>
    <span class="write-label abs" style="left:64px; top:272px">name, vorname</span>
    <span class="write-label abs" style="left:119px; top:272px">e-mail adresse</span>
  </div>
  <div class="fold-line abs" style="left:200px; top:0; height:286px"></div>

  <ul class="facts abs">
    <li class="fact">kalorienarm genießen</li>
    <li class="fact">100 % PUR, biologische milch und<br>joghurt aus der region</li>
    <li class="fact">keine künstlichen zusatzmittel.</li>
    <li class="fact">viel kalzium und eiweiss</li>
    <li class="fact">frische vitaminreiche toppings</li>
  </ul>

  <div class="social abs">
    <p class="social-text">jetzt freunde werden<br>www.freshcorner.example/fanpage<br>oder freundschaftsanfrage an<br>friends@fresh-corner.example schicken.</p>
  </div>
  <div class="social-mark abs" aria-hidden="true"></div>

  <div class="brand-mark abs" aria-hidden="true"></div>
  <p class="brand-name abs">fresh corner @ markt ecke</p>
  <p class="slogan abs">fresh corner makes you feel good</p>

  <h2 class="pass-title abs">frozen yoghurt pass</h2>
  <table class="stamps abs" aria-label="Stempelfelder">
    <tr>
      <td><span class="stamp-cup tone-berry" role="img" aria-label="Stempelfeld Becher"></span></td>
      <td><span class="stamp-cup tone-choc" role="img" aria-label="Stempelfeld Becher"></span></td>
      <td><span class="stamp-cup tone-orange" role="img" aria-label="Stempelfeld Becher"></span></td>
      <td><span class="stamp-cup tone-choc" role="img" aria-label="Stempelfeld Becher"></span></td>
      <td><span class="stamp-cup tone-berry" role="img" aria-label="Stempelfeld Becher"></span></td>
    </tr>
    <tr>
      <td><span class="stamp-cup tone-choc" role="img" aria-label="Stempelfeld Becher"></span></td>
      <td><span class="stamp-cup tone-berry" role="img" aria-label="Stempelfeld Becher"></span></td>
      <td><span class="stamp-cup tone-choc" role="img" aria-label="Stempelfeld Becher"></span></td>
      <td><span class="stamp-cup tone-orange" role="img" aria-label="Stempelfeld Becher"></span></td>
      <td class="stamp-free"><span class="stamp-cup tone-free" role="img" aria-label="Gratis-Becher"></span></td>
    </tr>
  </table>
  <p class="pass-note abs">beim kauf von 9 frozen yoghurt ihrer wahl erhalten sie einen gratis</p>
</section>

</body>
</html>
```